Organic rose water based skincare line in need of product label and packaging design

We are looking for a simple, clean, modern labeling and packaging design for 2 of our products. Our brand's demographic is upscale females ages 20-40. We want our packaging to be very minimalistic, and instagramable.

Product #1: Rose water facial spray "Lilac Mist"
Product #2: Rose water facial toner "The Late Hour"

Please see attached images for our current logo and label design. We have also added some images that inspire our branding.

Target Market(s)

trendy woman ages 20-40

Industry/Entity Type

Skin Care Product

Font styles to use
Serif
Sans Serif

Colors

Designer to choose only greyscale colors for use in the design.

Requirements
Must have
• Must have our logo, bottle size, product name on front and how to use and ingredient on the back. Please see project description and attached images for more information.
Should not have
• Too much going on or too many colors.

```html
<!DOCTYPE html>
<html lang="en">
<head>
<meta charset="utf-8">
<title>The Petal Studio — Product Labels and Packaging</title>
<link rel="stylesheet" href="https://fonts.googleapis.com/css2?family=Oswald:wght@300;400&family=Josefin+Sans:wght@300&family=Cormorant+Garamond:ital,wght@1,400&display=swap">
<style>
  :root {
    --ink: #111111;
    --ink-soft: #2a2a2a;
    --rule: #3a3a3a;
    --paper: #ffffff;
    --blush: #f9eef3;
    --bottle-edge: #d9d9d9;
    --bottle-fill: #fbfbfb;
    --trigger-dark: #1c1c1c;
    --trigger-mid: #3d3d3d;
    --art-tone: #e4d8de;
  }
  html, body {
    margin: 0;
    padding: 0;
    width: 1200px;
    height: 618px;
    overflow: hidden;
    background: var(--paper);
  }
  .canvas { display: block; width: 1200px; height: 618px; }
  .wordmark { font-family: "Oswald", sans-serif; font-weight: 300; fill: var(--ink); }
  .product-title { font-family: "Oswald", sans-serif; font-weight: 300; fill: var(--ink); letter-spacing: 0.12em; }
  .body-copy { font-family: "Josefin Sans", sans-serif; font-weight: 300; fill: var(--ink-soft); }
  .script-copy { font-family: "Cormorant Garamond", serif; font-style: italic; fill: var(--ink-soft); }
  .alt-title { font-family: "Josefin Sans", sans-serif; font-weight: 300; fill: var(--ink); letter-spacing: 0.14em; }
  .rule { stroke: var(--rule); stroke-width: 0.8; }
  .bottle-body { fill: url(#bottleShade); stroke: var(--bottle-edge); stroke-width: 1; }
  .box-panel { fill: var(--blush); stroke: #ece0e6; stroke-width: 1; }
</style>
</head>
<body>
<svg class="canvas" viewBox="0 0 1200 618" xmlns="http://www.w3.org/2000/svg">
  <defs>
    <linearGradient id="bottleShade" x1="0" x2="1">
      <stop offset="0" stop-color="#eeeeee"/>
      <stop offset="0.2" stop-color="var(--bottle-fill)"/>
      <stop offset="0.8" stop-color="var(--bottle-fill)"/>
      <stop offset="1" stop-color="#e8e8e8"/>
    </linearGradient>
    <linearGradient id="triggerShade" x1="0" y1="0" x2="0" y2="1">
      <stop offset="0" stop-color="var(--trigger-mid)"/>
      <stop offset="1" stop-color="var(--trigger-dark)"/>
    </linearGradient>
    <linearGradient id="artShade" x1="0" y1="0" x2="0" y2="1">
      <stop offset="0" stop-color="var(--art-tone)"/>
      <stop offset="1" stop-color="var(--blush)"/>
    </linearGradient>
  </defs>

  <!-- Title lockup studies -->
  <g class="title-studies">
    <text class="product-title" x="858" y="36" text-anchor="middle" font-size="31">LILAC</text>
    <text class="product-title" x="858" y="72" text-anchor="middle" font-size="25">MIST</text>
    <text class="alt-title" x="973" y="36" text-anchor="middle" font-size="28">LILAC</text>
    <text class="alt-title" x="973" y="70" text-anchor="middle" font-size="23">MIST</text>
    <text class="product-title" x="1094" y="36" text-anchor="middle" font-size="31" font-weight="400">LILAC</text>
    <text class="product-title" x="1094" y="76" text-anchor="middle" font-size="29">MIST</text>
  </g>

  <!-- Toner bottle, front -->
  <g class="bottle bottle--toner-front" transform="translate(126,0)">
    <rect role="img" aria-label="Black trigger spray head" x="-88" y="160" width="120" height="145" rx="10" fill="url(#triggerShade)"/>
    <path class="bottle-body" d="M-30,305 L30,305 L30,318 C55,325 67,340 67,365 L67,548 Q67,560 55,560 L-55,560 Q-67,560 -67,548 L-67,365 C-67,340 -55,325 -30,318 Z"/>
    <text class="wordmark" x="0" y="380" text-anchor="middle" font-size="11">the petal</text>
    <text class="wordmark" x="0" y="393" text-anchor="middle" font-size="11">studio</text>
    <text class="product-title" x="0" y="436" text-anchor="middle" font-size="18">THE</text>
    <text class="product-title" x="0" y="456" text-anchor="middle" font-size="18">LATE</text>
    <text class="product-title" x="0" y="476" text-anchor="middle" font-size="18">HOUR</text>
    <line class="rule" x1="-41" y1="489" x2="41" y2="489"/>
    <text class="body-copy" x="0" y="501" text-anchor="middle" font-size="10">organic rose</text>
    <text class="body-copy" x="0" y="513" text-anchor="middle" font-size="10">facial toner</text>
    <line class="rule" x1="-41" y1="517" x2="41" y2="517"/>
    <text class="body-copy" x="0" y="535" text-anchor="middle" font-size="10">2 oz / 60mL</text>
  </g>

  <!-- Toner bottle, back -->
  <g class="bottle bottle--toner-back" transform="translate(290,0)">
    <rect role="img" aria-label="Black trigger spray head" x="-88" y="160" width="120" height="145" rx="10" fill="url(#triggerShade)"/>
    <path class="bottle-body" d="M-30,305 L30,305 L30,318 C55,325 67,340 67,365 L67,548 Q67,560 55,560 L-55,560 Q-67,560 -67,548 L-67,365 C-67,340 -55,325 -30,318 Z"/>
    <g class="body-copy" font-size="7.5" text-anchor="middle">
      <text x="0" y="403">To use:</text>
      <text x="0" y="412.5">shake well.</text>
      <text x="0" y="422">apply a small amount of</text>
      <text x="0" y="431.5">toner to a clean cotton pad</text>
      <text x="0" y="441">+ gently sweep over your</text>
      <text x="0" y="450.5">face + neck</text>
    </g>
    <text class="body-copy" x="0" y="468" text-anchor="middle" font-size="10">witchhazel / rose</text>
    <g class="body-copy" font-size="7.5" text-anchor="middle">
      <text x="0" y="487">Benefits of use:</text>
      <text x="0" y="496.5">+ tightens skin</text>
      <text x="0" y="506">+ shrinks pores</text>
      <text x="0" y="515.5">+ prevents acne</text>
      <text x="0" y="525">+ treats discoloration</text>
      <text x="0" y="534.5">+ removes impurities</text>
    </g>
  </g>

  <!-- Toner box -->
  <g class="box box--toner">
    <rect class="box-panel" x="386" y="90" width="204" height="471"/>
    <text class="wordmark" x="413" y="140" font-size="22">the</text>
    <text class="wordmark" x="413" y="163" font-size="22">petal</text>
    <text class="wordmark" x="413" y="186" font-size="22">studio</text>
    <rect role="img" aria-label="Single-line rose illustration with long stem and leaf" x="505" y="239" width="73" height="307" rx="4" fill="url(#artShade)"/>
    <text class="product-title" x="450" y="381" text-anchor="middle" font-size="33">THE</text>
    <text class="product-title" x="450" y="419" text-anchor="middle" font-size="33">LATE</text>
    <text class="product-title" x="450" y="457" text-anchor="middle" font-size="33">HOUR</text>
    <line class="rule" x1="401" y1="476" x2="503" y2="476"/>
    <text class="body-copy" x="452" y="490" text-anchor="middle" font-size="13">organic rose</text>
    <text class="body-copy" x="452" y="506" text-anchor="middle" font-size="13">facial toner</text>
    <line class="rule" x1="401" y1="512" x2="503" y2="512"/>
    <text class="body-copy" x="451" y="534" text-anchor="middle" font-size="13">2 oz / 60mL</text>
  </g>

  <!-- Mist box -->
  <g class="box box--mist">
    <rect class="box-panel" x="611" y="90" width="204" height="471"/>
    <text class="wordmark" x="638" y="141" font-size="22">the</text>
    <text class="wordmark" x="638" y="164" font-size="22">petal</text>
    <text class="wordmark" x="638" y="187" font-size="22">studio</text>
    <rect role="img" aria-label="Single-line rose illustration with long stem and leaf" x="730" y="239" width="73" height="307" rx="4" fill="url(#artShade)"/>
    <text class="product-title" x="675" y="405" text-anchor="middle" font-size="33">LILAC</text>
    <text class="product-title" x="675" y="441" text-anchor="middle" font-size="28">MIST</text>
    <text class="script-copy" x="675" y="467" text-anchor="middle" font-size="10.5">rose water facial spray</text>
    <text class="body-copy" x="676" y="492" text-anchor="middle" font-size="13">organic rosewater</text>
    <text class="body-copy" x="676" y="506" text-anchor="middle" font-size="13">hydrating mist</text>
    <line class="rule" x1="626" y1="512" x2="727" y2="512"/>
    <text class="body-copy" x="676" y="534" text-anchor="middle" font-size="13">2 oz / 60mL</text>
  </g>

  <!-- Mist bottle, front -->
  <g class="bottle bottle--mist-front" transform="translate(925,0)">
    <rect role="img" aria-label="Black trigger spray head" x="-88" y="162" width="120" height="143" rx="10" fill="url(#triggerShade)"/>
    <path class="bottle-body" d="M-30,305 L30,305 L30,318 C55,325 67,340 67,365 L67,548 Q67,560 55,560 L-55,560 Q-67,560 -67,548 L-67,365 C-67,340 -55,325 -30,318 Z"/>
    <text class="wordmark" x="0" y="381" text-anchor="middle" font-size="11">the petal</text>
    <text class="wordmark" x="0" y="394" text-anchor="middle" font-size="11">studio</text>
    <text class="product-title" x="0" y="443" text-anchor="middle" font-size="18">LILAC</text>
    <text class="product-title" x="0" y="463" text-anchor="middle" font-size="16">MIST</text>
    <text class="script-copy" x="0" y="479" text-anchor="middle" font-size="6.5">rose water facial spray</text>
    <text class="body-copy" x="0" y="500" text-anchor="middle" font-size="10">organic rosewater</text>
    <text class="body-copy" x="0" y="512" text-anchor="middle" font-size="10">hydrating mist</text>
    <line class="rule" x1="-41" y1="517" x2="41" y2="517"/>
    <text class="body-copy" x="0" y="535" text-anchor="middle" font-size="10">2oz / 60mL</text>
  </g>

  <!-- Mist bottle, back -->
  <g class="bottle bottle--mist-back" transform="translate(1086,0)">
    <rect role="img" aria-label="Black trigger spray head" x="-88" y="162" width="120" height="143" rx="10" fill="url(#triggerShade)"/>
    <path class="bottle-body" d="M-30,305 L30,305 L30,318 C55,325 67,340 67,365 L67,548 Q67,560 55,560 L-55,560 Q-67,560 -67,548 L-67,365 C-67,340 -55,325 -30,318 Z"/>
    <g class="body-copy" font-size="7.5" text-anchor="middle">
      <text x="0" y="424">To use:</text>
      <text x="0" y="433.5">mist over</text>
      <text x="0" y="443">face + body + hair</text>
      <text x="0" y="452.5">as desired for hydration</text>
    </g>
    <text class="script-copy" x="0" y="472" text-anchor="middle" font-size="9.5">organic / rose / water</text>
    <g class="body-copy" font-size="7.5" text-anchor="middle">
      <text x="0" y="488">Benefits of use:</text>
      <text x="0" y="501">+ hydrates + fight acne</text>
      <text x="0" y="512">+ maintains skin's pH</text>
      <text x="0" y="523">+ strengthens skin cells</text>
      <text x="0" y="534">+ prevents fine lines &amp; wrinkles</text>
    </g>
  </g>
</svg>
</body>
</html>
```